Design Emoji directory website with a modern look

Please design the Emoji directory website to display a nice search box as well as design a nice search suggestion dropdown page. Example when you type keyword in Quorvex.
You can use Emojis in SVG file https://www.filebarrow.com/s/7kq2m9x4pLwz8tr/svg.rar?dl=0 to create designs.
The following are 7 example pages but please make sure the design is UNIQUE.
Main page example
https://glyphpond.info/
Content page example
https://glyphpond.info/smiling-face-with-smiling-eyes/
Category page example
https://glyphpond.info/smileys-and-emotion-category/
Holiday page example
https://glyphpond.info/holidays/
Static pages example
https://glyphpond.info/privacy-policy/
404 page not found example
https://glyphpond.info/category/
Search page example
https://glyphpond.info/?s=exchange+rate
Target Market(s)
web design
Industry/Entity Type
Website
Number of Pages Required
5+ page
Font styles to use
Other font styles liked:
- COMIC NEUE
Colors
Designer to choose colors to be used in the design.
Requirements
Must have
- Please make sure its unique, modern look, clean.
Should not have
- Do not use heavy graphics, we only use CSS style rules and SVG's emojis to make sure the site loads fast.

```html
<!DOCTYPE html>
<html lang="en">
<head>
<meta charset="utf-8">
<title>Glyphora Emojis</title>
<link rel="stylesheet" href="https://fonts.googleapis.com/css2?family=Didact+Gothic&family=Arimo:wght@400;700&display=swap">
<style>
:root{
  --navy:#15284a;
  --navy-deep:#0f1f3b;
  --green:#3ec47d;
  --badge:#4cc98a;
  --page:#f1f1f1;
  --card:#ffffff;
  --line:#e3e3e3;
  --ink:#222;
  --muted:#555;
  --blue:#1f6fc1;
  --star:#f58a1f;
  --footer:#262626;
  --footer-line:#444;
}
*{margin:0;padding:0;box-sizing:border-box}
html,body{width:1200px;height:3139px;overflow:hidden}
body{position:relative;background:var(--page);font-family:"Didact Gothic",sans-serif;color:var(--ink)}
.abs{position:absolute}

/* hero */
.hero{position:absolute;left:0;top:0;width:1200px;height:489px;background:linear-gradient(135deg,var(--navy-deep),var(--navy) 60%,#1b3358)}
.hero-art{position:absolute;left:760px;top:60px;width:420px;height:429px;border-radius:50% 40% 0 60%;background:radial-gradient(circle at 40% 40%,rgba(255,255,255,.05),rgba(255,255,255,0) 70%)}
.menu{left:144px;top:48px;width:26px}
.menu span{display:block;height:3px;background:#fff;margin-bottom:6px;border-radius:1px}
.brand{left:0;width:1200px;top:36px;text-align:center;color:#fff;font-size:44px;letter-spacing:1px}
.signup{left:886px;top:41px;width:169px;height:39px;border:2px solid #fff;border-radius:3px;color:#fff;font-family:Arimo,sans-serif;font-size:13px;line-height:35px;text-align:center;letter-spacing:.3px}
.hero-title{left:0;width:1200px;top:170px;text-align:center;color:#fff;font-size:56px;font-weight:normal}
.hero-title em{font-style:normal;color:var(--green)}
.hero-lede{left:0;width:1200px;top:248px;text-align:center;color:#fff;font-size:16px;line-height:24px}
.search{left:339px;top:327px;width:522px;height:45px;background:#fff;border-radius:23px;padding:0 21px;display:flex;align-items:center;justify-content:space-between;font-size:14px;color:#333}

/* emoji cards */
.card{position:absolute;width:299px;height:316px;background:var(--card);border:1px solid var(--line)}
.card .grid{position:absolute;left:21px;top:24px;width:257px;height:228px;display:grid;grid-template-columns:repeat(3,1fr);grid-template-rows:repeat(3,1fr);gap:12px 11px}
.grid span{border-radius:8px;background:var(--a)}
.grid span:nth-child(3n+2){background:var(--b)}
.grid span:nth-child(3n){background:var(--c)}
.grid.figures span{width:44px;justify-self:center;border-radius:22px 22px 8px 8px}
.grid.round span{width:64px;justify-self:center;border-radius:50%}
.card .foot{position:absolute;left:0;right:0;bottom:0;height:40px;border-top:1px solid var(--line);display:flex;align-items:center;justify-content:space-between;padding:0 21px;font-size:13px;font-weight:bold}
.card .foot .see{font-weight:normal;font-size:13px;display:flex;align-items:center;gap:6px}
.badge{background:var(--badge);color:#fff;font-size:11px;padding:3px 9px;border-radius:2px}
.tip{position:absolute;left:107px;top:17px;width:88px;height:74px;background:#fff;border:1px solid var(--green);border-radius:3px;font-size:8px;text-align:center;padding-top:50px;line-height:9px;box-shadow:0 2px 6px rgba(0,0,0,.15)}

/* pagination */
.pager{left:443px;top:1974px;display:flex;gap:8px;align-items:flex-end}
.pager span{width:29px;height:29px;border:1px solid #ccc;background:#fff;font-size:12px;line-height:27px;text-align:center;font-family:Arimo,sans-serif}
.pager .arrow{background:#b9b9b9;border-color:#b9b9b9}
.pager .dots{border:none;background:none;width:14px;color:#999}

/* testimonials */
.voices{position:absolute;left:0;top:2098px;width:1200px;height:629px;background:#fff}
.voices h2{position:absolute;top:76px;width:1200px;text-align:center;font-weight:normal;font-size:34px}
.voices .rule{position:absolute;left:565px;top:136px;width:70px;height:3px;background:var(--blue)}
.quote{position:absolute;top:196px;width:290px;height:271px;background:#fff;border-radius:10px;box-shadow:0 2px 14px rgba(0,0,0,.12);text-align:center;padding:80px 22px 0;font-family:Arimo,sans-serif;font-size:14px;line-height:21px;color:var(--muted)}
.quote::after{content:"";position:absolute;left:137px;bottom:-8px;border:8px solid transparent;border-bottom:0;border-top-color:#fff}
.quote .mark{position:absolute;left:122px;top:16px;width:46px;height:46px;border-radius:50%;background:#222}
.who{position:absolute;top:492px;width:290px;text-align:center;font-family:Arimo,sans-serif;font-size:14.5px}
.who .stars{color:var(--star);font-size:15px;letter-spacing:2px;margin-top:6px}

/* footer */
.footer{position:absolute;left:0;top:2727px;width:1200px;height:412px;background:var(--footer);color:#fff}
.footer .divider{position:absolute;top:0;width:1px;height:227px;background:var(--footer-line)}
.footer .hline{position:absolute;left:144px;top:227px;width:911px;height:1px;background:var(--footer-line)}
.contact{position:absolute;top:47px;width:300px;text-align:center}
.contact .ring{width:58px;height:58px;border:2px solid #fff;border-radius:50%;margin:0 auto 20px;display:flex;align-items:center;justify-content:center}
.contact b{display:block;font-weight:normal;font-size:15px;font-family:Arimo,sans-serif}
.contact small{display:block;font-size:14px;margin-top:5px}
.social{position:absolute;top:276px;left:533px;display:flex;gap:11px}
.social span{width:37px;height:37px;border:2px solid #fff;border-radius:50%;display:flex;align-items:center;justify-content:center}
.copy{position:absolute;top:338px;width:1200px;text-align:center;font-size:15px}
</style>
</head>
<body>

<header class="hero">
  <div class="hero-art" role="img" aria-label="Faint illustration of a figure in motion"></div>
  <div class="abs menu"><span></span><span></span><span></span></div>
  <div class="abs brand">Glyphora</div>
  <div class="abs signup">SIGNUP FOR FREE</div>
  <h1 class="abs hero-title">Glyphora <em>Emojis</em></h1>
  <p class="abs hero-lede">Nemo enim ipsam voluptatem quia voluptas sit aspernatur aut odit aut<br>fugit, sed quia consequuntur magni dolores eos</p>
  <div class="abs search">
    <span>Search emojis</span>
    <svg width="18" height="18" viewBox="0 0 18 18"><circle cx="7.5" cy="7.5" r="5.5" fill="none" stroke="#222" stroke-width="2.4"/><line x1="11.5" y1="11.5" x2="16" y2="16" stroke="#222" stroke-width="2.6" stroke-linecap="round"/></svg>
  </div>
</header>

<main>
  <div class="card" style="left:129px;top:560px"><div class="grid" role="img" aria-label="Grid of nine country flag emojis" style="--a:#d8303f;--b:#2a2a2a;--c:#2a8a3e"><span></span><span></span><span></span><span style="background:#1d3a9e"></span><span style="background:#243a7a"></span><span style="background:#2a9a4a"></span><span style="background:#e9e9e9"></span><span style="background:#2c8a3a"></span><span style="background:#e8c21f"></span></div><div class="foot">Flag<span class="see">See all <span class="badge">151</span></span></div></div>
  <div class="card" style="left:452px;top:560px"><div class="grid figures" role="img" aria-label="Grid of nine weightlifting emojis" style="--a:#e5534b;--b:#3b6fb5;--c:#c93c4a"><span></span><span></span><span></span><span></span><span></span><span></span><span></span><span></span><span></span></div><div class="tip">Sed ut perspiciatis unde omnis</div><div class="foot">Fitness<span class="see">See all <span class="badge">151</span></span></div></div>
  <div class="card" style="left:774px;top:560px"><div class="grid figures" role="img" aria-label="Grid of nine golfer emojis" style="--a:#f08a3c;--b:#8c9aa5;--c:#4aa0d8"><span></span><span></span><span></span><span></span><span></span><span></span><span></span><span></span><span></span></div><div class="foot">Golf<span class="see">See all <span class="badge">151</span></span></div></div>

  <div class="card" style="left:129px;top:904px"><div class="grid round" role="img" aria-label="Grid of nine symbol emojis" style="--a:#3a3a3a;--b:#d93a3a;--c:#f5c242"><span></span><span></span><span></span><span style="background:#55a5e5"></span><span style="background:#8a4a2a"></span><span style="background:#b06a3e"></span><span style="background:#a9d2ef"></span><span style="background:#5ba9e5"></span><span style="background:#e33a3a"></span></div><div class="foot">Nemo enim ipsam<span class="see">See all <span class="badge">151</span></span></div></div>
  <div class="card" style="left:452px;top:904px"><div class="grid" role="img" aria-label="Grid of nine office object emojis" style="--a:#3aa05a;--b:#3b6fb5;--c:#6fb2e8"><span></span><span></span><span></span><span style="background:#a0522d"></span><span style="background:#2b2b2b"></span><span style="background:#3a3f4a"></span><span style="background:#2d7fd0"></span><span style="background:#f2c14e"></span><span style="background:#a9abb0"></span></div><div class="foot">Nemo enim ipsam<span class="see">See all <span class="badge">151</span></span></div></div>
  <div class="card" style="left:774px;top:904px"><div class="grid" role="img" aria-label="Grid of nine desk item emojis" style="--a:#f6d99a;--b:#6fa5d6;--c:#7a6fb5"><span></span><span></span><span></span><span style="background:#9aa3ab"></span><span style="background:#5ba9e5"></span><span style="background:#4b535c"></span><span style="background:#7f8a94"></span><span style="background:#d8dde2"></span><span style="background:#8a969f"></span></div><div class="foot">Nemo enim ipsam<span class="see">See all <span class="badge">151</span></span></div></div>

  <div class="card" style="left:129px;top:1249px"><div class="grid" role="img" aria-label="Grid of nine mountain biker emojis" style="--a:#5ab05a;--b:#6bb84e;--c:#7ab85a"><span></span><span></span><span></span><span style="background:#8c8f93"></span><span style="background:#8c8f93"></span><span style="background:#8c8f93"></span><span></span><span></span><span></span></div><div class="foot">Nemo enim ipsam<span class="see">See all <span class="badge">151</span></span></div></div>
  <div class="card" style="left:452px;top:1249px"><div class="grid" role="img" aria-label="Grid of nine travel emojis" style="--a:#3b7ec2;--b:#5ba9e5;--c:#7a8a98"><span></span><span></span><span></span><span style="background:#a9c4d8"></span><span style="background:#9cc1de"></span><span style="background:#d8343c"></span><span style="background:#3a9ad9"></span><span style="background:#8a96a0"></span><span style="background:#d8343c"></span></div><div class="foot">Nemo enim ipsam<span class="see">See all <span class="badge">151</span></span></div></div>
  <div class="card" style="left:774px;top:1249px"><div class="grid" role="img" aria-label="Grid of nine vehicle emojis" style="--a:#d8343c;--b:#7bb7e8;--c:#f5c242"><span></span><span></span><span style="border-radius:50%"></span><span style="background:#5ba9e5"></span><span style="background:#d8343c"></span><span style="background:#f2b632"></span><span style="background:#d8343c"></span><span style="background:#a5b4c0"></span><span style="background:#b8734a"></span></div><div class="foot">Nemo enim ipsam<span class="see">See all <span class="badge">151</span></span></div></div>

  <div class="card" style="left:129px;top:1592px"><div class="grid figures" role="img" aria-label="Grid of nine kneeling person emojis" style="--a:#7ab85a;--b:#8e6ac2;--c:#f08a3c"><span></span><span></span><span></span><span></span><span></span><span></span><span></span><span></span><span></span></div><div class="foot">Nemo enim ipsam<span class="see">See all <span class="badge">151</span></span></div></div>
  <div class="card" style="left:452px;top:1592px"><div class="grid figures" role="img" aria-label="Grid of nine people emojis" style="--a:#b5734a;--b:#e0e4ea;--c:#f3c9a8"><span></span><span></span><span></span><span style="background:#9aa3ab"></span><span style="background:#f08a3c"></span><span></span><span style="background:#5a6470"></span><span style="background:#3b6fb5"></span><span></span></div><div class="foot">Nemo enim ipsam<span class="see">See all <span class="badge">151</span></span></div></div>
  <div class="card" style="left:774px;top:1592px"><div class="grid" role="img" aria-label="Grid of nine clothing and fantasy emojis" style="--a:#d8343c;--b:#3b6fb5;--c:#3a8ad0"><span></span><span></span><span></span><span style="background:#9aa0a6"></span><span style="background:#c9303a"></span><span style="background:#3a8ad0"></span><span style="background:#5ba9e5"></span><span style="background:#3d4a6b"></span><span style="background:#8a969f"></span></div><div class="foot">Nemo enim ipsam<span class="see">See all <span class="badge">151</span></span></div></div>

  <nav class="abs pager">
    <span class="arrow"><svg width="10" height="10" viewBox="0 0 10 10"><path d="M7 1 3 5l4 4z" fill="#fff"/></svg></span>
    <span>1</span><span>2</span><span>3</span><span>4</span><span>5</span><span class="dots">...</span><span>10</span>
    <span class="arrow"><svg width="10" height="10" viewBox="0 0 10 10"><path d="M3 1l4 4-4 4z" fill="#fff"/></svg></span>
  </nav>
</main>

<section class="voices">
  <h2>What clients say about us?</h2>
  <div class="rule"></div>

  <div class="quote" style="left:144px"><div class="mark"><svg width="46" height="46" viewBox="0 0 46 46"><path d="M14 30v-6c0-4 2-7 6-8v3c-2 1-3 2-3 4h3v7zm11 0v-6c0-4 2-7 6-8v3c-2 1-3 2-3 4h3v7z" fill="#fff"/></svg></div>Sed ut perspiciatis unde omnis iste natus error sit voluptatem accuntium doloremque laudantium, totam rem aperiam, eaque ipsa quae ab illo itore veritatis et quasi architecto beatae vitae dicta sunt explicabo. Nemo enim ipsam voluptatem quia voluptas sit aspernatur aut odit aut</div>
  <div class="quote" style="left:454px"><div class="mark"><svg width="46" height="46" viewBox="0 0 46 46"><path d="M14 30v-6c0-4 2-7 6-8v3c-2 1-3 2-3 4h3v7zm11 0v-6c0-4 2-7 6-8v3c-2 1-3 2-3 4h3v7z" fill="#fff"/></svg></div>Sed ut perspiciatis unde omnis iste natus error sit voluptatem accuntium doloremque laudantium, totam rem aperiam, eaque ipsa quae ab illo itore veritatis et quasi architecto beatae vitae dicta sunt explicabo. Nemo enim ipsam voluptatem quia voluptas sit aspernatur aut odit aut</div>
  <div class="quote" style="left:765px"><div class="mark"><svg width="46" height="46" viewBox="0 0 46 46"><path d="M14 30v-6c0-4 2-7 6-8v3c-2 1-3 2-3 4h3v7zm11 0v-6c0-4 2-7 6-8v3c-2 1-3 2-3 4h3v7z" fill="#fff"/></svg></div>Sed ut perspiciatis unde omnis iste natus error sit voluptatem accuntium doloremque laudantium, totam rem aperiam, eaque ipsa quae ab illo itore veritatis et quasi architecto beatae vitae dicta sunt explicabo. Nemo enim ipsam voluptatem quia voluptas sit aspernatur aut odit aut</div>

  <div class="who" style="left:144px">Nemo enim ipsam<div class="stars">★★★★★</div></div>
  <div class="who" style="left:454px">Nemo enim ipsam<div class="stars">★★★★★</div></div>
  <div class="who" style="left:765px">Nemo enim ipsam<div class="stars">★★★★★</div></div>
</section>

<footer class="footer">
  <div class="divider" style="left:499px"></div>
  <div class="divider" style="left:730px"></div>
  <div class="hline"></div>

  <div class="contact" style="left:173px">
    <div class="ring"><svg width="24" height="28" viewBox="0 0 24 28"><path d="M12 1C6 1 2 5.5 2 11c0 7 10 16 10 16s10-9 10-16C22 5.5 18 1 12 1z" fill="#fff"/><circle cx="12" cy="11" r="4" fill="#262626"/></svg></div>
    <b>ADDRESS</b><small>27 Lantern Row, Mossbrook Lane</small>
  </div>
  <div class="contact" style="left:455px">
    <div class="ring"><svg width="26" height="26" viewBox="0 0 26 26"><path d="M6 2l4 1 2 6-3 2c1 3 4 6 7 7l2-3 6 2 1 4c-1 3-3 4-5 4C11 25 1 15 2 6c0-2 1-4 4-4z" fill="#fff"/></svg></div>
    <b>PHONE</b><small>1-555-0142-7788</small>
  </div>
  <div class="contact" style="left:739px">
    <div class="ring"><svg width="28" height="20" viewBox="0 0 28 20"><rect x="1" y="1" width="26" height="18" rx="2" fill="#fff"/><path d="M2 3l12 9 12-9" fill="none" stroke="#262626" stroke-width="2"/></svg></div>
    <b>EMAIL</b><small>hello@glyphora.com</small>
  </div>

  <div class="social" aria-label="Social links">
    <span><svg width="16" height="16" viewBox="0 0 16 16"><circle cx="4" cy="8" r="2.2" fill="#fff"/><circle cx="12" cy="3.5" r="2.2" fill="#fff"/><circle cx="12" cy="12.5" r="2.2" fill="#fff"/><path d="M4 8l8-4.5M4 8l8 4.5" stroke="#fff" stroke-width="1.4"/></svg></span>
    <span><svg width="16" height="16" viewBox="0 0 16 16"><circle cx="4" cy="8" r="2.2" fill="#fff"/><circle cx="12" cy="3.5" r="2.2" fill="#fff"/><circle cx="12" cy="12.5" r="2.2" fill="#fff"/><path d="M4 8l8-4.5M4 8l8 4.5" stroke="#fff" stroke-width="1.4"/></svg></span>
    <span><svg width="16" height="16" viewBox="0 0 16 16"><circle cx="4" cy="8" r="2.2" fill="#fff"/><circle cx="12" cy="3.5" r="2.2" fill="#fff"/><circle cx="12" cy="12.5" r="2.2" fill="#fff"/><path d="M4 8l8-4.5M4 8l8 4.5" stroke="#fff" stroke-width="1.4"/></svg></span>
  </div>
  <div class="copy">Glyphora © 2020 All Rights Reserved | term and condition</div>
</footer>

</body>
</html>
```